Premium Juice and Wine Bottle Label

We require a premium label design for a Burgundy style wine bottle - the design should reflect pure and organic theme, with a reference to New Zealand blueberries. The winning design will look high-end, simple but sophisticated. Our logo is attached, refer :

https://www.rvcellar.co.nz and https://www.halopu.co.nz/wines/details/coming-soon-showcase/2018

for inspiration.

Target Market(s)

High-end retail grocery stores, wine shops, bars.

Requirements
Must have
• Label should leave enough space for barcode and nutrients/ingredients etc. Reference to New Zealand, natural-beverage, be very high-end in design. Refer links in project description for inspiration. Refer to attached logo, which must be used - feel free to change colour in order to obtain the best high-class design.
Nice to have
• N/A.
Should not have
• Cartoons or pictures of berries.

```html
<!DOCTYPE html>
<html lang="en">
<head>
<meta charset="utf-8">
<title>Kerrow Lane Pinot Noir – Label Set</title>
<link rel="stylesheet" href="https://fonts.googleapis.com/css2?family=Barlow+Semi+Condensed:wght@400;500&family=Lobster+Two:ital,wght@1,700&family=Merriweather:ital,wght@0,400;1,400&family=Inter:wght@600;700&display=swap">
<style>
  :root {
    --stage: #1d1d1e;
    --violet: #5f4b8b;
    --violet-deep: #4f3d7c;
    --violet-light: #7159a3;
    --gold: #d8bd84;
    --gold-deep: #b89a5f;
    --lavender: #ddd3f0;
    --paper: #ffffff;
    --ink: #111111;
  }
  * { box-sizing: border-box; margin: 0; padding: 0; }
  html, body {
    width: 1200px;
    height: 925px;
    overflow: hidden;
    background: var(--stage);
  }
  .canvas {
    position: relative;
    width: 1200px;
    height: 925px;
    background: var(--stage);
  }

  /* Colour swatch */
  .swatch {
    position: absolute;
    left: 476px;
    top: 0;
    width: 248px;
    height: 185px;
    background: var(--paper);
  }
  .swatch__chip {
    height: 139px;
    background: var(--violet);
  }
  .swatch__brand {
    margin: 9px 0 0 15px;
    font-family: "Inter", sans-serif;
    font-weight: 700;
    font-size: 11.5px;
    line-height: 14px;
    color: var(--ink);
    letter-spacing: 0.02em;
  }
  .swatch__name {
    margin: 1px 0 0 15px;
    font-family: "Inter", sans-serif;
    font-weight: 600;
    font-size: 9.5px;
    line-height: 12px;
    color: var(--ink);
  }

  /* Front label */
  .front-label {
    position: absolute;
    left: 110px;
    top: 340px;
    width: 340px;
    height: 416px;
    overflow: hidden;
  }
  .label-pattern {
    position: absolute;
    inset: 0;
    background: linear-gradient(115deg, var(--violet-deep) 0%, var(--violet) 55%, var(--violet-light) 100%);
  }
  .brand {
    position: absolute;
    top: 40px;
    left: 0;
    right: 0;
    display: flex;
    justify-content: center;
    align-items: center;
    gap: 8px;
  }
  .brand__mark {
    width: 10px;
    height: 10px;
    background: var(--gold);
  }
  .brand__name {
    font-family: "Merriweather", serif;
    font-size: 20px;
    color: var(--gold);
  }
  .title-frame {
    position: absolute;
    left: 84px;
    top: 123px;
    width: 172px;
    height: 172px;
    border: 3px solid var(--gold);
    background: rgba(95, 75, 139, 0.85);
    text-align: center;
    padding-top: 14px;
  }
  .title-frame__origin {
    font-family: "Merriweather", serif;
    font-style: italic;
    font-size: 10px;
    color: var(--gold-deep);
  }
  .title-frame__style {
    margin-top: 8px;
    font-family: "Barlow Semi Condensed", sans-serif;
    font-weight: 400;
    font-size: 33px;
    line-height: 36px;
    color: var(--gold);
    letter-spacing: 0.01em;
  }
  .title-frame__variety {
    margin-top: 2px;
    font-family: "Lobster Two", cursive;
    font-style: italic;
    font-weight: 700;
    font-size: 20px;
    color: var(--gold-deep);
    letter-spacing: 0.04em;
  }
  .title-frame__vintage {
    margin-top: 2px;
    font-family: "Merriweather", serif;
    font-size: 14px;
    color: var(--gold);
    letter-spacing: 0.05em;
  }
  .front-label__facts {
    position: absolute;
    left: 88px;
    right: 88px;
    bottom: 36px;
    display: flex;
    justify-content: space-between;
    font-family: "Merriweather", serif;
    font-style: italic;
    font-size: 10px;
    color: var(--lavender);
  }

  /* Back labels */
  .back-label {
    position: absolute;
    top: 340px;
    height: 416px;
    overflow: hidden;
    border-radius: 6px;
  }
  .back-label--story { left: 760px; width: 118px; }
  .back-label--info { left: 976px; width: 126px; }
  .back-label__copy {
    position: absolute;
    writing-mode: vertical-rl;
    transform: rotate(180deg);
    font-family: "Merriweather", serif;
    font-style: italic;
    font-size: 9px;
    line-height: 10.5px;
    color: var(--lavender);
  }
  .back-label--story .back-label__copy {
    left: 20px;
    bottom: 30px;
    height: 340px;
    width: 72px;
  }
  .back-label--info .back-label__copy {
    left: 26px;
    bottom: 30px;
    height: 256px;
    width: 84px;
  }
  .barcode-space {
    position: absolute;
    left: 33px;
    top: 0;
    width: 76px;
    height: 118px;
    background: linear-gradient(90deg, #e6e6e6, #ffffff 60%, #dcdcdc);
  }
</style>
</head>
<body>
<main class="canvas">

  <aside class="swatch">
    <div class="swatch__chip"></div>
    <p class="swatch__brand">CHROMAREF</p>
    <p class="swatch__name">21-4406 Dusk Iris</p>
  </aside>

  <section class="front-label">
    <div class="label-pattern" role="img" aria-label="Faint line pattern of blueberries, blossoms and leaves on violet"></div>
    <div class="brand">
      <span class="brand__mark"></span>
      <span class="brand__name">Kerrow Lane</span>
    </div>
    <div class="title-frame">
      <p class="title-frame__origin">New Zealand</p>
      <h1 class="title-frame__style">BURGUNDY<br>WINE</h1>
      <p class="title-frame__variety">Pinot Noir</p>
      <p class="title-frame__vintage">2019</p>
    </div>
    <div class="front-label__facts">
      <span>13.5% vol.</span>
      <span>750ml.</span>
    </div>
  </section>

  <section class="back-label back-label--story">
    <div class="label-pattern" role="img" aria-label="Faint line pattern of blueberries and leaves on violet"></div>
    <p class="back-label__copy">Grown on sunlit slopes and picked by hand, this Pinot Noir carries notes of dark berry, soft spice and cool earth. Aged gently in French oak, it pours smooth and bright. Serve slightly cool with roast lamb, mushrooms or aged cheese.</p>
  </section>

  <section class="back-label back-label--info">
    <div class="label-pattern" role="img" aria-label="Faint line pattern of blueberries and leaves on violet"></div>
    <div class="barcode-space"></div>
    <p class="back-label__copy">Made from organic fruit with care for the land and the water around it. Contains sulphites. Best enjoyed within eight years of vintage. Store on its side away from light and heat. Please enjoy responsibly.</p>
  </section>

</main>
</body>
</html>
```